Banner Ad Needed For Real Estate Lending Firm

We are taking out a banner ad on one of the most highly trafficked real estate websites in New York. The ad will be 970x250. Display format will be JPEG or animated GIF, but original art files will be required as well from the winning designer.

Granite Path Lending (or GPL) is one of the largest "hard money lenders" for real estate investors on the East Coast of the US. We lend for the following real estate investments: 1) Fix And Flip 2) New Construction 3) Cash Out Refinance. We close in 2-10 days. More information can be found on our website here: http://www.gpl7.example/

Our goal is to help small business owners, real estate investors, and commercial contractors quickly and efficiently finance their business activities. Our local hard money loan programs are tailored to your unique project needs. We fund fix and flip, new construction, and cash out refinance projects for non-owner occupied properties.

Target Market(s)

Real Estate Agents, Real Estate Investors, Mortgage Brokers, Other Real Estate Professionals

Industry/Entity Type

Real Estate

Font styles to use
Sans Serif

Requirements
Must have
• Must incorporate the fact that we close deals very fast (2 - 10 days), finance the following these 2 main types of investments (Fix and Flip, New Construction), and mention that Brokers can make up to 2.5 Points.
• See attached style guide for basic colors and fonts.
Nice to have
• Animated GIF might be a great feature!

```html
<!DOCTYPE html>
<html lang="en">
<head>
<meta charset="UTF-8">
<title>Granite Path Lending – Hard Money Lenders Banner</title>
<link rel="stylesheet" href="https://fonts.googleapis.com/css2?family=Rubik:wght@400;500;600&family=Roboto+Slab:wght@500;700;800&display=swap">
<style>
  :root {
    --page-bg: #f4f5f5;
    --white: #ffffff;
    --teal: #4db6a0;
    --teal-deep: #3aa38d;
    --petrol: #1c6478;
    --petrol-dark: #164f60;
    --ink-teal: #2f7f6f;
    --panel-top: #ffffff;
    --panel-bottom: #eef1f1;
    --divider: #c9d3d3;
  }
  * { margin: 0; padding: 0; box-sizing: border-box; }
  html, body {
    width: 1200px; height: 850px; overflow: hidden;
    background: var(--page-bg);
    font-family: "Rubik", Arial, sans-serif;
  }
  ul { list-style: none; }
  .banner {
    position: absolute; left: 40px; top: 280px;
    width: 1120px; height: 290px;
    background: var(--white);
    overflow: hidden;
    box-shadow: 0 6px 18px rgba(0,0,0,0.12);
  }

  .offer-panel {
    position: absolute; left: 783px; top: 0; z-index: 0;
    width: 337px; height: 290px;
    background: linear-gradient(180deg, var(--panel-top), var(--panel-bottom));
    border-left: 1px solid var(--divider);
  }
  .banner-shapes { position: absolute; inset: 0; z-index: 1; }
  .couple-photo { position: absolute; inset: 0; z-index: 1; }
  .house-in-hand {
    position: absolute; left: 684px; top: 166px; z-index: 2;
    width: 192px; height: 124px;
  }

  .brand {
    position: absolute; left: 487px; top: 18px; z-index: 3;
    display: flex; align-items: center; gap: 14px;
  }
  .brand-square { width: 54px; height: 54px; background: var(--ink-teal); }
  .brand-name {
    color: var(--ink-teal);
    font-weight: 600; font-size: 17px; line-height: 22px;
    text-transform: uppercase;
  }

  .headline-top {
    position: absolute; left: 487px; top: 100px; z-index: 3;
    font-weight: 600; font-size: 38px; color: var(--teal);
    letter-spacing: 0.3px;
  }
  .headline-main {
    position: absolute; left: 484px; top: 136px; z-index: 3;
    font-family: "Roboto Slab", "Rockwell", serif;
    font-weight: 800; font-size: 68px; line-height: 1;
    color: var(--petrol);
    letter-spacing: -0.5px;
  }

  .contact {
    position: absolute; left: 487px; top: 232px; z-index: 3;
    color: var(--white);
  }
  .contact-phone {
    display: flex; align-items: center; gap: 3px;
    font-weight: 600; font-size: 27px; line-height: 30px;
  }
  .contact-web {
    display: flex; align-items: center; gap: 6px;
    font-size: 11px; letter-spacing: 7px; margin-top: 1px;
  }

  .offer-title {
    position: absolute; left: 63px; top: 19px;
    width: 214px; height: 38px;
    border: 2px solid var(--teal); border-radius: 5px;
    box-shadow: 0 2px 4px rgba(0,0,0,0.15);
    background: var(--white);
    font-family: "Roboto Slab", "Rockwell", serif; font-weight: 500;
    font-size: 16px; color: var(--ink-teal);
    display: flex; align-items: center; justify-content: center;
  }
  .loan-types {
    position: absolute; left: 8px; top: 86px;
    width: 320px; display: flex; justify-content: space-between;
  }
  .loan-type {
    width: 106px; display: flex; flex-direction: column; align-items: center;
    font-family: "Roboto Slab", "Rockwell", serif; font-weight: 500;
    font-size: 12.5px; line-height: 15px; color: var(--ink-teal);
    text-align: center;
  }
  .loan-type + .loan-type { border-left: 1px dashed var(--divider); }
  .loan-icon {
    width: 42px; height: 42px; margin-bottom: 12px;
    filter: drop-shadow(0 2px 2px rgba(0,0,0,0.25));
  }
  .broker-note {
    position: absolute; left: 70px; top: 196px; width: 222px;
    text-align: center; color: var(--petrol);
    font-weight: 500; font-size: 19px; line-height: 21px;
  }
  .close-note {
    position: absolute; left: 70px; top: 244px; width: 222px;
    text-align: center; color: var(--ink-teal);
    font-weight: 400; font-size: 12.5px; line-height: 15px;
  }
  .accent-rule {
    position: absolute; left: 875px; top: 276px; z-index: 1;
    width: 245px; height: 5px; background: var(--petrol);
  }
</style>
</head>
<body>
  <section class="banner" aria-label="Granite Path Lending hard money lenders banner">
    <aside class="offer-panel">
      <p class="offer-title">Real estate investments:</p>
      <ul class="loan-types">
        <li class="loan-type">
          <svg class="loan-icon" viewBox="0 0 42 42" aria-hidden="true">
            <circle cx="21" cy="21" r="20" fill="var(--petrol-dark)"/>
            <path d="M21 10v13M16 15l5-5 5 5" fill="none" stroke="#fff" stroke-width="2.4" stroke-linecap="round" stroke-linejoin="round"/>
            <path d="M13 21v8h16v-8" fill="none" stroke="#fff" stroke-width="2.4" stroke-linejoin="round"/>
          </svg>
          Fix And<br>Flip
        </li>
        <li class="loan-type">
          <svg class="loan-icon" viewBox="0 0 42 42" aria-hidden="true">
            <circle cx="21" cy="21" r="20" fill="var(--petrol-dark)"/>
            <path d="M11 20l10-8 10 8v10H11z" fill="#fff"/>
            <path d="M21 27l-3.4-3.2c-1-1-.3-2.7 1.1-2.7.9 0 1.6.5 2.3 1.3.7-.8 1.4-1.3 2.3-1.3 1.4 0 2.1 1.7 1.1 2.7z" fill="var(--petrol-dark)"/>
          </svg>
          New<br>Construction
        </li>
        <li class="loan-type">
          <svg class="loan-icon" viewBox="0 0 42 42" aria-hidden="true">
            <circle cx="21" cy="21" r="20" fill="var(--petrol-dark)"/>
            <rect x="12" y="12" width="18" height="18" fill="none" stroke="#fff" stroke-width="2.2"/>
            <path d="M14 28l9-11 5 11z" fill="#fff"/>
          </svg>
          Cash Out<br>Refinance
        </li>
      </ul>
      <p class="broker-note">Brokers can make<br>up to 2.5 Points</p>
      <p class="close-note">We close in 2–10 days</p>
    </aside>

    <svg class="banner-shapes" width="1120" height="290" viewBox="0 0 1120 290" aria-hidden="true">
      <polygon points="330,0 357,0 430,226 880,226 880,290 465,290" fill="var(--teal)"/>
      <polygon points="430,226 880,226 880,230 436,230" fill="var(--teal-deep)"/>
    </svg>

    <svg class="couple-photo" width="1120" height="290" viewBox="0 0 1120 290"
         role="img" aria-label="Photo of a smiling couple sitting on a lawn in front of a yellow house">
      <defs>
        <linearGradient id="photoTones" x1="0" y1="0" x2="0" y2="1">
          <stop offset="0" stop-color="#a98a6c"/>
          <stop offset="0.45" stop-color="#d9b85a"/>
          <stop offset="0.75" stop-color="#8cbf68"/>
          <stop offset="1" stop-color="#5e9a3e"/>
        </linearGradient>
      </defs>
      <polygon points="0,0 330,0 465,290 0,290" fill="url(#photoTones)"/>
    </svg>

    <svg class="house-in-hand" viewBox="0 0 192 124" role="img"
         aria-label="Illustration of a small model house resting on an open hand">
      <defs>
        <radialGradient id="houseHandTones" cx="0.55" cy="0.6" r="0.55">
          <stop offset="0" stop-color="#d9a07e" stop-opacity="0.9"/>
          <stop offset="0.6" stop-color="#e2b79a" stop-opacity="0.55"/>
          <stop offset="1" stop-color="#e2b79a" stop-opacity="0"/>
        </radialGradient>
      </defs>
      <ellipse cx="104" cy="76" rx="96" ry="58" fill="url(#houseHandTones)"/>
    </svg>

    <div class="brand">
      <span class="brand-square" aria-hidden="true"></span>
      <p class="brand-name">Granite<br>Path<br>Lending LLC</p>
    </div>

    <p class="headline-top">Hard money</p>
    <h1 class="headline-main">lenders</h1>

    <div class="contact">
      <p class="contact-phone">
        <svg width="16" height="16" viewBox="0 0 16 16" aria-hidden="true">
          <circle cx="8" cy="8" r="7" fill="none" stroke="#fff" stroke-width="1.4"/>
          <path d="M5.6 4.5c.6-.4 1.1-.2 1.3.3l.5 1.1c.1.4 0 .7-.3.9l-.4.3c.3.9 1 1.7 1.9 2.1l.3-.4c.2-.3.6-.4.9-.2l1 .5c.5.3.6.8.2 1.3-.6.7-1.5.9-2.4.4-1.6-.8-2.8-2.1-3.4-3.8-.3-.9-.1-1.8.4-2.5z" fill="#fff"/>
        </svg>
        555.014.2087
      </p>
      <p class="contact-web">
        <svg width="13" height="13" viewBox="0 0 14 14" aria-hidden="true">
          <g fill="none" stroke="#fff" stroke-width="1">
            <circle cx="7" cy="7" r="6"/>
            <ellipse cx="7" cy="7" rx="2.6" ry="6"/>
            <path d="M1 7h12M2 4h10M2 10h10"/>
          </g>
        </svg>
        www.gpl7.example
      </p>
    </div>

    <span class="accent-rule" aria-hidden="true"></span>
  </section>
</body>
</html>
```